Profile Card Layout/Design Template

We recently ran a workshop with a client and during that workshop we developed some typical profiles of their target audience using flip chart paper. We now want to turn the profiles into professionally designed A5 cards we can then print and give to the client, therefore we require the profile card layout template to be designed so that in the future we can insert the profile data and images in-house.
Attached are 3 files.
1. persona_sallysocial.jpg is one of profiles we want to convert
2. profilecards.png is an example of the type of design/layout we need to convert the flip chart data to.
3. our company logo
So the layout needs to provide space for
- the profile data specified in persona_sallysocial.jpg
- some additional space for a profile summary/overview not currently shown in persona_sallysocial.jpg but
- an image/photo of the profiled person
- a placeholder for the clients logo
- a placeholder for our company logo
- placeholders for appropriate images to compliment the profile
Happy to consider both portrait and landscape designs
Would be good but not essential if we could change colours of specific elements of the design to compliment the clients corporate colours. So for instance our current clients corporate colours are #b50700, #001739 & #000000

```html
<!DOCTYPE html>
<html lang="en">
<head>
<meta charset="UTF-8">
<title>Sally Social – Profile Card</title>
<link rel="stylesheet" href="https://fonts.googleapis.com/css2?family=PT+Sans:wght@400;700&family=Kalam:wght@400&display=swap">
<style>
  :root {
    --card-border: #b50700;
    --panel: #f59bc6;
    --ink: #1a1a1a;
    --frame-line: #6e6e6e;
    --placeholder-line: #9a9a9a;
    --photo-tone: #c9a89a;
    --clip-tone: #b9bcc0;
    --page: #ffffff;
  }
  * { box-sizing: border-box; margin: 0; padding: 0; }
  html, body { width: 1200px; height: 848px; overflow: hidden; background: var(--page); }
  body { font-family: "PT Sans", Arial, sans-serif; color: var(--ink); }

  .profile-card { position: relative; width: 1200px; height: 848px; }
  .card-border {
    position: absolute; left: 50px; top: 50px; width: 1100px; height: 750px;
    border: 4px solid var(--card-border); border-radius: 36px;
  }

  .section-heading {
    position: absolute; font-weight: 700; font-size: 19px; text-transform: uppercase;
    letter-spacing: 0.3px; border-bottom: 2px solid var(--ink); padding-bottom: 1px; line-height: 1.1;
  }
  .panel { position: absolute; background: var(--panel); border-radius: 22px; }

  .bullet-list { list-style: none; padding: 22px 0 0 18px; }
  .bullet-list li { position: relative; font-size: 14px; line-height: 20px; padding-left: 22px; }
  .bullet-list li::before {
    content: ""; position: absolute; left: 0; top: 6px; width: 9px; height: 9px;
    border-radius: 50%; background: var(--ink);
  }

  .motivates-heading { left: 88px; top: 72px; }
  .motivates-panel { left: 74px; top: 116px; width: 268px; height: 190px; }
  .behaviour-heading { left: 92px; top: 340px; }
  .behaviour-panel { left: 74px; top: 376px; width: 274px; height: 140px; }
  .frustration-heading { left: 92px; top: 574px; }
  .frustration-panel { left: 74px; top: 614px; width: 274px; height: 146px; }

  .portrait-panel { left: 364px; top: 116px; width: 368px; height: 372px; }
  .snapshot-frame {
    position: absolute; left: 500px; top: 100px; width: 220px; height: 280px;
    background: var(--page); transform: rotate(3deg);
    box-shadow: 2px 3px 6px rgba(0,0,0,0.35); padding: 14px 14px 0;
  }
  .portrait-photo { width: 192px; height: 232px; background: linear-gradient(160deg, #e7d3c6, var(--photo-tone) 60%, #b8332e); }
  .paper-clip {
    position: absolute; left: 674px; top: 84px; width: 20px; height: 50px;
    background: var(--clip-tone); border-radius: 10px; transform: rotate(38deg);
  }
  .goal-text {
    position: absolute; left: 376px; top: 346px; width: 350px;
    font-family: "Kalam", cursive; font-size: 18px; line-height: 24px;
  }
  .goal-label { display: block; margin-bottom: 10px; }

  .pain-heading { left: 372px; top: 506px; }
  .pain-panel { left: 364px; top: 544px; width: 322px; height: 148px; }

  .image-slot { position: absolute; border: 1.5px solid var(--placeholder-line); background: var(--page); }
  .slot-small { top: 706px; width: 74px; height: 74px; }

  .mood-slot { position: absolute; border: 2px solid var(--frame-line); background: var(--page); }

  .persona-name {
    position: absolute; left: 770px; top: 218px; font-size: 54px; font-weight: 700;
    letter-spacing: 1px; line-height: 1;
  }

  .summary-heading { left: 762px; top: 312px; }
  .summary-panel { left: 750px; top: 360px; width: 374px; height: 272px; }
  .summary-text { padding: 14px 60px 0 20px; font-size: 17px; line-height: 26px; text-indent: 62px; }

  .client-logo-slot {
    position: absolute; left: 740px; top: 660px; width: 130px; height: 122px;
    border: 1.5px solid var(--placeholder-line); display: flex; align-items: center; justify-content: center;
    font-size: 14px;
  }

  .agency-credit {
    position: absolute; left: 916px; top: 728px; width: 210px;
    font-size: 11px; line-height: 14px; font-weight: 400; color: var(--ink);
  }
</style>
</head>
<body>
<main class="profile-card">
  <div class="card-border"></div>

  <h2 class="section-heading motivates-heading">What motivates me?</h2>
  <div class="panel motivates-panel">
    <ul class="bullet-list">
      <li>Friendship/relationship</li>
      <li>Making me most of every moment</li>
      <li>Value for money</li>
      <li>Well organised</li>
      <li>Fun environment</li>
    </ul>
  </div>

  <h2 class="section-heading behaviour-heading">Behaviour</h2>
  <div class="panel behaviour-panel">
    <ul class="bullet-list">
      <li>Busy</li>
      <li>No flashy technology</li>
    </ul>
  </div>

  <h2 class="section-heading frustration-heading">Frustration/Fear/...</h2>
  <div class="panel frustration-panel">
    <ul class="bullet-list">
      <li>Doesn't like down time</li>
      <li>Too competitive</li>
      <li>Wasting my time</li>
      <li>Who's looking after the kids</li>
      <li>I won't be able to play?</li>
    </ul>
  </div>

  <div class="panel portrait-panel"></div>
  <div class="snapshot-frame">
    <div class="portrait-photo" role="img" aria-label="Portrait photo of the profiled person"></div>
  </div>
  <div class="paper-clip" role="img" aria-label="Paper clip holding the photo"></div>
  <p class="goal-text"><span class="goal-label">GOAL:</span>Have fun being physically<br>active with like minded people.</p>

  <h2 class="section-heading pain-heading">Pain points</h2>
  <div class="panel pain-panel">
    <ul class="bullet-list">
      <li>Things must just worth - functional</li>
      <li>You won't be good enough</li>
      <li>Scared of being hurt</li>
      <li>No hit</li>
      <li>Knowledge of rules</li>
    </ul>
  </div>

  <div class="image-slot slot-small" style="left:368px"></div>
  <div class="image-slot slot-small" style="left:464px"></div>
  <div class="image-slot slot-small" style="left:560px"></div>

  <div class="mood-slot" style="left:798px;top:124px;width:82px;height:82px;transform:rotate(-8deg)"></div>
  <div class="mood-slot" style="left:888px;top:74px;width:80px;height:78px"></div>
  <div class="mood-slot" style="left:982px;top:122px;width:80px;height:80px;transform:rotate(12deg)"></div>

  <h1 class="persona-name">SALLY SOCIAL</h1>

  <h2 class="section-heading summary-heading">Summary/Overview</h2>
  <div class="panel summary-panel">
    <p class="summary-text">Summary or overview write in here.</p>
  </div>

  <div class="client-logo-slot">Client's logo</div>

  <p class="agency-credit">Designed and powered by Bright Summit</p>
</main>
</body>
</html>
```